Tallis Ecological Works New Website Design

I need a new website for a Environmental Project Company based in Sydney Australia, working throughout South East Asia.I've attached the company logo, please try & incorporate these colours or use complimentary colours. I've attached a word doc with design brief.I'm going to use Wix, so please ensure files are suitable.Thankyou.

Number of Pages Required

5+ page

Colors

Designer to choose colors to be used in the design.

Requirements
Must have
• Refer to Word Document
Nice to have
• Refer to Word Document
Should not have
• Not to be dark

```html
<!DOCTYPE html>
<html lang="en">
<head>
<meta charset="utf-8">
<title>Tallis Ecological Works</title>
<link rel="stylesheet" href="https://fonts.googleapis.com/css2?family=Jost:wght@300;400;500;600&display=swap">
<style>
:root{
  --line:#141414;
  --white:#ffffff;
  --ink:#2a2f22;
  --text:#3a3a3a;
  --forest:#2f5a1c;
  --teal:#1f9c78;
  --logo-bg:#efefef;
  --sage:#e8eae2;
  --mint:#d9f2eb;
  --mist:#f1f1f1;
  --dark:#161616;
  --footer:#efefef;
}
*{box-sizing:border-box;margin:0;padding:0}
html,body{width:1200px;height:2317px;overflow:hidden}
body{font-family:"Jost",sans-serif;font-weight:300;color:var(--text);background:var(--footer)}
.page{width:1200px;height:2317px;position:relative}
.row{position:absolute;left:0;width:1200px;display:grid;gap:4px;background:var(--line);border:3px solid var(--line);border-bottom:none}
.row>*{overflow:hidden}
.header{top:0;height:82px;grid-template-columns:369px 1fr}
.brand{background:var(--logo-bg);display:flex;align-items:center;justify-content:center;gap:14px}
.brand-mark{width:52px;height:52px;border-radius:50%;background:var(--forest)}
.brand-name{font-weight:500;font-size:17px;letter-spacing:2px;color:var(--forest);text-transform:uppercase;line-height:1.15;width:200px}
.nav{background:var(--white);display:flex;justify-content:flex-end;align-items:center;gap:34px;padding-right:56px}
.nav a{font-size:19px;font-weight:400;color:var(--ink);text-decoration:none}
.nav a.active{color:var(--forest)}
.row-1{top:79px;height:515px;grid-template-columns:536px 369px 1fr}
.row-2{top:591px;height:516px;grid-template-columns:355px 473px 1fr}
.row-3{top:1104px;height:513px;grid-template-columns:465px 406px 1fr}
.row-4{top:1614px;height:515px;grid-template-columns:397px 396px 1fr}
.social{top:2126px;height:91px;grid-template-columns:397px 396px 1fr;border-bottom:3px solid var(--line)}
.photo{width:100%;height:100%}
.panel{display:flex;flex-direction:column;align-items:center;justify-content:center;text-align:center;position:relative}
.panel h2{font-weight:300;font-size:31px;line-height:1.25;color:var(--ink)}
.panel h2 .accent{color:var(--teal)}
.panel p{font-size:17px;line-height:35px;color:var(--text)}
.read-more{position:absolute;bottom:40px;left:0;right:0;text-align:center;font-size:15px;font-weight:600;color:var(--teal);text-decoration:none;letter-spacing:.3px}
.welcome{background:var(--white);padding:0 40px 60px}
.welcome h2{margin-bottom:34px}
.products{background:var(--sage);padding:0 70px 50px}
.products h3{font-weight:300;font-size:21px;color:var(--teal);margin:16px 0 20px}
.products p{font-size:16px;line-height:29px}
.arrow{position:absolute;top:270px;width:14px;height:18px}
.arrow.prev{left:36px}.arrow.next{right:36px}
.vision{background:var(--mint);padding:0 90px}
.vision p,.mission p{font-size:16px;line-height:29px;margin-top:32px}
.mission{background:var(--mist);padding:0 60px}
.focus{background:var(--dark);display:flex;align-items:center;padding-left:26px}
.focus ul{list-style:none}
.focus li{display:flex;align-items:flex-start;gap:14px;color:#f2f2f2;font-size:16px;line-height:21px;margin:20px 0}
.focus li svg{flex:none;margin-top:2px}
.social a{background:var(--white);display:flex;align-items:center;justify-content:center;gap:10px;font-size:26px;font-weight:400;color:var(--ink);text-decoration:none}
.social-dot{width:18px;height:18px;background:var(--ink)}
.footer{position:absolute;top:2217px;left:0;width:1200px;height:100px;display:flex;align-items:center;justify-content:center;font-size:16px;color:var(--text);font-weight:400}
</style>
</head>
<body>
<div class="page">
  <header class="row header">
    <div class="brand"><span class="brand-mark"></span><span class="brand-name">Tallis Ecological Works</span></div>
    <nav class="nav">
      <a class="active" href="#">Home</a><a href="#">Who We Are</a><a href="#">Services</a><a href="#">Products</a><a href="#">News</a><a href="#">Contact</a>
    </nav>
  </header>

  <section class="row row-1">
    <div class="photo" role="img" aria-label="Solar panels in a green field with a wind turbine at sunrise" style="background:linear-gradient(180deg,#7fa2c2 0%,#e9b98a 35%,#6c8aa6 55%,#3f6b1f 75%,#2d5a12 100%)"></div>
    <div class="panel welcome">
      <h2><span class="accent">Welcome to</span> Tallis<br>Ecological Works</h2>
      <p>Lorem ipsum dolor sit amet, con<br>etur adipiscing elit, sed do eiusmod<br>tempor incididunt ut labore et dolore<br>magna aliquenim ad minim.</p>
      <a class="read-more" href="#">READ MORE ›</a>
    </div>
    <div class="photo" role="img" aria-label="Office corridor with a living green wall" style="background:linear-gradient(90deg,#2f5a22 0%,#4f7d33 45%,#c9cccc 60%,#e5e7e7 100%)"></div>
  </section>

  <section class="row row-2">
    <div class="photo" role="img" aria-label="Lettuce seedlings growing in hydroponic channels" style="background:linear-gradient(160deg,#8fbf45 0%,#5a9a2a 40%,#7b4a2a 60%,#6ea83a 100%)"></div>
    <div class="panel products" role="group" aria-label="Products">
      <h2>Products</h2>
      <h3>Sustainable Food</h3>
      <p>Lorem ipsum dolor sit amet, conetur adipiin g elit, sed do eiusmod tempor incididunt ut labore et dolore magna aliquenim ad mLorem ipsum dolor sit am conetur adipisc elit.</p>
      <svg class="arrow prev" viewBox="0 0 14 18"><path d="M10 3 4 9l6 6" fill="none" stroke="#222" stroke-width="2"/></svg>
      <svg class="arrow next" viewBox="0 0 14 18"><path d="M4 3l6 6-6 6" fill="none" stroke="#222" stroke-width="2"/></svg>
      <a class="read-more" href="#">READ MORE ›</a>
    </div>
    <div class="photo" role="img" aria-label="Circular fish farm pens on a fjord below green hills" style="background:linear-gradient(180deg,#b8cde0 0%,#5d7a4a 18%,#2d5f86 30%,#1e4a72 100%)"></div>
  </section>

  <section class="row row-3">
    <div class="panel vision">
      <h2><span class="accent">Vision</span> Statement</h2>
      <p>Our Vision is to make it easy for everyone to minimise their environmental impact by providing information, technology, packaged green solutions &amp; helping innovation flourish.</p>
    </div>
    <div class="photo" role="img" aria-label="Field of leafy green crops under a blue sky" style="background:linear-gradient(180deg,#5f9ad8 0%,#a9cbe6 33%,#5f9a3a 40%,#3f7a22 70%,#6aa83c 100%)"></div>
    <div class="focus">
      <ul>
        <li><svg width="15" height="15" viewBox="0 0 16 16"><circle cx="8" cy="8" r="8" fill="#f2f2f2"/><path d="M4.5 8.2 7 10.6l4.6-5" fill="none" stroke="#161616" stroke-width="2"/></svg>Sustainable food.</li>
        <li><svg width="15" height="15" viewBox="0 0 16 16"><circle cx="8" cy="8" r="8" fill="#f2f2f2"/><path d="M4.5 8.2 7 10.6l4.6-5" fill="none" stroke="#161616" stroke-width="2"/></svg>Sustainable / Renewable power.</li>
        <li><svg width="15" height="15" viewBox="0 0 16 16"><circle cx="8" cy="8" r="8" fill="#f2f2f2"/><path d="M4.5 8.2 7 10.6l4.6-5" fill="none" stroke="#161616" stroke-width="2"/></svg>Water quality &amp; treatment.</li>
        <li><svg width="15" height="15" viewBox="0 0 16 16"><circle cx="8" cy="8" r="8" fill="#f2f2f2"/><path d="M4.5 8.2 7 10.6l4.6-5" fill="none" stroke="#161616" stroke-width="2"/></svg>Air quality.</li>
        <li><svg width="15" height="15" viewBox="0 0 16 16"><circle cx="8" cy="8" r="8" fill="#f2f2f2"/><path d="M4.5 8.2 7 10.6l4.6-5" fill="none" stroke="#161616" stroke-width="2"/></svg>Investing in green infrastructure<br>&amp; projects.</li>
        <li><svg width="15" height="15" viewBox="0 0 16 16"><circle cx="8" cy="8" r="8" fill="#f2f2f2"/><path d="M4.5 8.2 7 10.6l4.6-5" fill="none" stroke="#161616" stroke-width="2"/></svg>Education.</li>
      </ul>
    </div>
  </section>

  <section class="row row-4">
    <div class="photo" role="img" aria-label="Gardener planting a potted seedling in a garden bed" style="background:linear-gradient(160deg,#3b5a2a 0%,#6a7d4a 35%,#d9d6cc 50%,#6b5a44 75%,#4a3a2a 100%)"></div>
    <div class="panel mission">
      <h2><span class="accent">Mission</span> Statement</h2>
      <p>Working with people to minimise the environmental impact of humans on the earth without sacrificing lifestyle and helping innovation flourish.</p>
    </div>
    <div class="photo" role="img" aria-label="Wind turbines on a hillside above clouds at dusk" style="background:linear-gradient(180deg,#6f8fb8 0%,#d9b89a 35%,#9a8aa0 50%,#5a4a3a 70%,#3a3a22 100%)"></div>
  </section>

  <nav class="row social">
    <a href="#"><span class="social-dot"></span>Chirpline</a>
    <a href="#"><span class="social-dot"></span>Workweave</a>
    <a href="#"><span class="social-dot"></span>Circlebook</a>
  </nav>

  <footer class="footer">© 2019 All Rights Are Reserved.Terms of Use | Privacy Policy</footer>
</div>
</body>
</html>
```